Zuvo Decor

There is a sample provided with the arabic text of the business card. please copy paste the same text and the same Logo (The two triangles) Just try to incorproate the Brown background attached (you are free to change the colors) Id like the colors to be mainly shades of black and red.

```html
<!DOCTYPE html>
<html lang="ar">
<head>
<meta charset="utf-8">
<title>Zuvo Decor – Business Card</title>
<link rel="stylesheet" href="https://fonts.googleapis.com/css2?family=Aref+Ruqaa:wght@400;700&family=Oswald:wght@600&family=Roboto:wght@500&family=Tajawal:wght@400&display=swap">
<style>
  :root {
    --page: #ebe8e4;
    --red: #d11f45;
    --red-deep: #b8163a;
    --red-light: #e0335a;
    --charcoal: #252624;
    --white: #ffffff;
    --ink: #1e1e1e;
  }
  * { margin: 0; padding: 0; box-sizing: border-box; }
  html, body {
    width: 1125px; height: 1200px; overflow: hidden;
    background: var(--page);
  }
  .canvas { position: relative; width: 1125px; height: 1200px; }

  .card {
    position: absolute; left: 171px; width: 826px; height: 472px;
    overflow: hidden;
    box-shadow: 0 3px 8px rgba(0,0,0,.25);
  }
  .card--front { top: 106px; background: var(--charcoal); }
  .card--back { top: 639px; }

  .pattern-field {
    position: absolute; inset: 0;
    background: radial-gradient(ellipse at 50% 45%, var(--red-light) 0%, var(--red) 55%, var(--red-deep) 100%);
  }
  .card--front .pattern-field { bottom: auto; height: 263px; }

  .brand {
    position: absolute; top: 185px; left: 0; width: 100%;
    text-align: center;
    font-family: "Oswald", sans-serif; font-weight: 600;
    font-size: 38px; letter-spacing: 1px; color: var(--white);
  }

  .divider {
    position: absolute; top: 263px; left: 0; width: 100%; height: 9px;
    background: var(--white);
  }
  .divider-pointer {
    position: absolute; top: 271px; left: 128px; width: 0; height: 0;
    border-left: 10px solid transparent; border-right: 10px solid transparent;
    border-top: 14px solid var(--white);
  }

  .owner {
    position: absolute; top: 296px; right: 525px;
    direction: rtl; text-align: center; color: var(--white);
    font-family: "Aref Ruqaa", serif;
  }
  .owner-name { font-size: 27px; font-weight: 700; line-height: 1.3; }
  .owner-title { font-size: 18px; line-height: 1.2; }

  .phone {
    position: absolute; top: 402px; left: 66px;
    display: flex; align-items: center; gap: 6px;
    font-family: "Roboto", sans-serif; font-weight: 500;
    font-size: 20px; color: var(--white);
  }
  .phone svg { width: 18px; height: 18px; }

  .credentials {
    list-style: none; direction: rtl; text-align: right;
    font-family: "Tajawal", sans-serif; color: var(--white);
  }
  .credentials--front {
    position: absolute; top: 318px; right: 68px;
    font-size: 20px; line-height: 27px;
  }
  .credentials--back {
    position: absolute; top: 162px;
    font-size: 25px; line-height: 33px;
  }
  .credentials--back.col-right { right: 85px; }
  .credentials--back.col-left { right: 442px; }
  .credentials--back li { display: flex; align-items: center; gap: 12px; }
  .credentials--back li::after {
    content: ""; width: 9px; height: 9px; border-radius: 50%;
    background: var(--ink); flex: none;
  }
</style>
</head>
<body>
<main class="canvas">

  <section class="card card--front">
    <div class="pattern-field" role="img" aria-label="Red backdrop with a fine mosaic of small squares and dots"></div>
    <div class="brand">Zuvo Decor</div>
    <div class="divider"></div>
    <div class="divider-pointer"></div>

    <div class="owner">
      <p class="owner-name">المهندس / سامر نبيل الراشد</p>
      <p class="owner-title">أستاذ جامعي</p>
    </div>

    <p class="phone">
      <svg viewBox="0 0 24 24" aria-hidden="true"><path fill="#fff" d="M6.6 10.8a15.1 15.1 0 0 0 6.6 6.6l2.2-2.2c.3-.3.7-.4 1-.2 1.1.4 2.3.6 3.6.6.6 0 1 .4 1 1V20c0 .6-.4 1-1 1A17 17 0 0 1 3 4c0-.6.4-1 1-1h3.5c.6 0 1 .4 1 1 0 1.3.2 2.5.6 3.6.1.3 0 .7-.2 1l-2.3 2.2z"/></svg>
      35550142 / 66550198
    </p>

    <ul class="credentials credentials--front">
      <li>ماجستير هندسة ديكور</li>
      <li>دبلوم عالي فن تشكيلي</li>
      <li>جامعة المرسم (باريس)</li>
      <li>استشارات هندسية - فنية</li>
    </ul>
  </section>

  <section class="card card--back">
    <div class="pattern-field" role="img" aria-label="Red backdrop with a fine mosaic of small squares and dots"></div>
    <ul class="credentials credentials--back col-right">
      <li>ماجستير هندسة ديكور</li>
      <li>دبلوم عالي فن تشكيلي</li>
      <li>جامعة المرسم (باريس)</li>
      <li>استشارات هندسية - فنية</li>
    </ul>
    <ul class="credentials credentials--back col-left">
      <li>ماجستير هندسة ديكور</li>
      <li>دبلوم عالي فن تشكيلي</li>
      <li>جامعة المرسم (باريس)</li>
      <li>استشارات هندسية - فنية</li>
    </ul>
  </section>

</main>
</body>
</html>
```